Mobile Recording Studio needs business cards

Open to seeing a creative design, but I want to emphasis my logo and minimize the name/title and company information. Possible a fully black background on card.

My company is a mobile sound recording studio. ok to include a my trailer (actual or cartoon) on the card. My initial thought is more straight forward, but a good design will win me over.

SPECS:
CMYK color mode
High (300ppi) raster effect.
cover bleed area
please deliver: Illustrator file with layers and a pdf at completion.

Name and info for the business card:

Dallin Perry
ADR Mixer

email: Dallin@MixVault.com

address:
248 - 5170 East Hollister
Vancouver, BC V5R 2J4

phone:
604.518.2093 office

website:
www.MixVault.com

FB: @MixVault

Instagram: @TheMixVault

Industry/Entity Type

Television Production

Contact Information for Business Card

Dallin Perry
ADR Mixer

email: Dallin@MixVault.com

address:
248 - 5170 East Hollister
Vancouver, BC V5R 2J4

phone:
604.518.2093 office

website:
www.MixVault.com

FB: @MixVault

Instagram: @TheMixVault

Colors

Designer to choose colors to be used in the design.

Requirements
Must have
• emphasis my logo and minimize the name/title and company information.
• SPECS:
• CMYK color mode
• High (300ppi) raster effect.
• cover bleed area
• please deliver: Illustrator file with layers and a pdf at completion.
Nice to have
• maybe include the following:
• all black background or black theme
• my work trailer (actual or cartoon) refer to Instagram: @TheMixVault

```html
<!DOCTYPE html>
<html lang="en">
<head>
<meta charset="utf-8">
<title>MixVault Business Card</title>
<link href="https://fonts.googleapis.com/css2?family=Cinzel:wght@400;600&family=Open+Sans:wght@400&display=swap" rel="stylesheet">
<style>
  :root {
    --backdrop: #2f2f2f;
    --card-black: #050505;
    --card-sheen: #1c1c1c;
    --silver: #c9c9c9;
    --text-light: #e6e6e6;
    --text-muted: #bdbdbd;
    --photo-dark: #0c0d0e;
    --photo-mid: #3a3d40;
    --photo-light: #8a8c8e;
  }
  * { margin: 0; padding: 0; box-sizing: border-box; }
  html, body { width: 1200px; height: 942px; overflow: hidden; background: var(--backdrop); }
  .stage {
    width: 1200px; height: 942px;
    display: flex; flex-direction: column; align-items: center; justify-content: center;
    gap: 56px;
  }
  .card {
    width: 640px; height: 366px;
    position: relative; overflow: hidden;
    box-shadow: 0 14px 30px rgba(0,0,0,.45);
  }
  .card-front {
    background:
      linear-gradient(115deg, transparent 30%, rgba(255,255,255,.07) 42%, transparent 52%),
      radial-gradient(ellipse at 50% 40%, var(--card-sheen), var(--card-black) 70%);
    color: var(--text-light);
    display: flex; flex-direction: column; align-items: center;
  }
  .brand {
    margin-top: 96px;
    font-family: "Cinzel", serif;
    font-weight: 600;
    font-size: 58px;
    letter-spacing: 2px;
    color: var(--silver);
  }
  .holder-name {
    margin-top: 30px;
    font-family: "Cinzel", serif;
    font-size: 17px;
    letter-spacing: 1.5px;
  }
  .holder-title {
    margin-top: 3px;
    font-family: "Cinzel", serif;
    font-size: 11px;
    letter-spacing: 1.5px;
    color: var(--text-muted);
  }
  .contact {
    margin-top: 22px;
    font-family: "Open Sans", sans-serif;
    font-size: 10.5px;
    color: var(--text-muted);
    display: flex; flex-direction: column; align-items: center; gap: 6px;
  }
  .contact-row { display: flex; gap: 12px; align-items: center; }
  .contact-item { display: inline-flex; align-items: center; gap: 4px; }
  .icon { width: 10px; height: 10px; fill: var(--text-muted); }
  .card-back {
    background: var(--photo-dark);
  }
  .trailer-photo {
    position: absolute; inset: 0;
    background:
      radial-gradient(ellipse at 62% 55%, var(--photo-light) 0%, var(--photo-mid) 35%, transparent 70%),
      linear-gradient(180deg, var(--photo-dark) 0%, #1e2022 55%, var(--photo-dark) 100%);
    opacity: .85;
  }
  .social {
    position: absolute; top: 18px; left: 22px;
    display: flex; gap: 18px;
    font-family: "Open Sans", sans-serif;
    font-size: 10.5px;
    color: var(--text-light);
  }
  .social-item { display: inline-flex; align-items: center; gap: 5px; }
  .social-mark { width: 9px; height: 9px; background: var(--text-light); border-radius: 1px; }
</style>
</head>
<body>
<main class="stage">
  <section class="card card-front">
    <div class="brand">MixVault</div>
    <div class="holder-name">Dallin Perry</div>
    <div class="holder-title">ADR Mixer</div>
    <div class="contact">
      <div class="contact-row">
        <span class="contact-item">
          <svg class="icon" viewBox="0 0 10 10"><path d="M2 0.5 L3.6 0.5 L4.2 3 L3 3.8 Q4 6 6.2 7 L7 5.8 L9.5 6.4 L9.5 8 Q9.5 9.5 8 9.5 Q0.5 9 0.5 2 Q0.5 0.5 2 0.5 Z"/></svg>
          604.518.2093
        </span>
        <span class="contact-item">
          <svg class="icon" viewBox="0 0 10 10"><path d="M0.5 2 H9.5 V8 H0.5 Z M1 2.4 L5 5.4 L9 2.4" stroke="#050505" stroke-width="0.8"/></svg>
          Dallin@MixVault.com
        </span>
        <span class="contact-item">
          <svg class="icon" viewBox="0 0 10 10"><circle cx="5" cy="5" r="4.5" fill="none" stroke="#bdbdbd" stroke-width="1"/><path d="M0.5 5 H9.5 M5 0.5 Q2 5 5 9.5 M5 0.5 Q8 5 5 9.5" fill="none" stroke="#bdbdbd" stroke-width="0.7"/></svg>
          www.MixVault.com
        </span>
      </div>
      <div class="contact-row">
        <span class="contact-item">
          <svg class="icon" viewBox="0 0 10 10"><path d="M5 0.3 Q1.5 0.3 1.5 3.8 Q1.5 6 5 9.8 Q8.5 6 8.5 3.8 Q8.5 0.3 5 0.3 Z M5 2.4 A1.4 1.4 0 1 0 5 5.2 A1.4 1.4 0 1 0 5 2.4 Z" fill-rule="evenodd"/></svg>
          248 - 5170 East Hollister Vancouver, BC V5R 2J4
        </span>
      </div>
    </div>
  </section>

  <section class="card card-back">
    <div class="trailer-photo" role="img" aria-label="Night photograph of the mobile recording studio trailer parked beside a truck"></div>
    <div class="social">
      <span class="social-item"><span class="social-mark"></span>@MixVault</span>
      <span class="social-item"><span class="social-mark"></span>@TheMixVault</span>
    </div>
  </section>
</main>
</body>
</html>
```